Brightwater Ledger Services, Inc.

Tax, Accounting and Bookkeeping Services

“We provide our services, with you next mortgage in mind”

Special pricing available for all Mortgage Loan Customers!!

President / CEO Marcus Delaney

Primary service provider with over 27 years of experience

Call directly for more information: (240) 555-0182

Or email at: mdelaney@brightwaterledger-example.com

```html
<!DOCTYPE html>
<html lang="en">
<head>
<meta charset="utf-8">
<title>Brightwater Ledger Services – Tax, Accounting and Bookkeeping</title>
<link rel="stylesheet" href="https://fonts.googleapis.com/css2?family=Poppins:ital,wght@0,400;0,500;0,600;0,700;0,800;1,700&display=swap">
<style>
  :root {
    --backdrop: #666666;
    --paper: #ffffff;
    --navy: #17447c;
    --gold: #b1a236;
    --ink: #0b0b0b;
    --muted: #9a9a9a;
    --photo-light: #eef1f4;
  }
  * { margin: 0; padding: 0; box-sizing: border-box; }
  html, body {
    width: 1200px; height: 1165px; overflow: hidden;
    background: var(--backdrop);
    font-family: "Poppins", sans-serif;
  }
  .flyer {
    position: absolute; left: 167px; top: 149px;
    width: 866px; height: 867px;
    background: var(--paper); overflow: hidden;
  }
  .office-photo {
    position: absolute; left: 0; top: 0; width: 866px; height: 300px;
    background: linear-gradient(180deg, var(--photo-light) 0%, #f4f6f8 60%, var(--paper) 100%);
  }
  .brand {
    position: absolute; left: 37px; top: 95px; width: 260px;
    display: flex; flex-direction: column; align-items: center; gap: 8px;
  }
  .brand-row { display: flex; align-items: center; gap: 10px; }
  .brand-dot { width: 34px; height: 34px; border-radius: 50%; background: var(--navy); flex: none; }
  .brand-name {
    font-weight: 700; font-size: 20px; line-height: 1.15; color: var(--navy);
  }
  .brand-est { font-weight: 600; font-size: 10px; letter-spacing: 2px; color: var(--navy); }
  .headline {
    position: absolute; left: 47px; top: 206px;
    font-weight: 800; font-size: 79px; line-height: 70px;
    letter-spacing: -0.5px; color: var(--navy);
  }
  .headline .accent { color: var(--gold); }
  .tagline {
    position: absolute; left: 47px; top: 430px;
    font-weight: 600; font-size: 25px; line-height: 34px; color: var(--ink);
  }
  .offer {
    position: absolute; left: 48px; top: 510px; width: 435px; height: 74px;
    background: var(--gold); border-radius: 13px;
    padding: 6px 0 0 15px;
    font-weight: 500; font-size: 25px; line-height: 32px; color: var(--paper);
  }
  .leader { position: absolute; left: 48px; top: 625px; }
  .leader-role { font-weight: 500; font-size: 20px; color: var(--muted); line-height: 26px; }
  .leader-name { font-weight: 700; font-style: italic; font-size: 28px; color: var(--gold); line-height: 34px; }
  .leader-bio { margin-top: 10px; font-weight: 500; font-size: 16.5px; line-height: 21px; color: var(--muted); }
  .contact { position: absolute; left: 45px; top: 770px; z-index: 2; }
  .contact-line { display: flex; align-items: center; gap: 8px; }
  .contact-icon { width: 24px; height: 24px; flex: none; }
  .contact-phone { font-weight: 700; font-size: 31px; color: var(--ink); line-height: 40px; }
  .contact-email { font-weight: 500; font-size: 12px; color: var(--ink); line-height: 24px; white-space: nowrap; }
  .contact-line + .contact-line { margin-top: 4px; }
  .accent-circle { position: absolute; left: 0; top: 0; }
  .portrait { position: absolute; }
  .portrait-ceo {
    left: 585px; top: 411px; width: 267px; height: 456px;
    border-radius: 130px 130px 0 0;
    background: linear-gradient(180deg, #5a3b2a 0%, #8d8f93 40%, #a4a6aa 100%);
  }
  .portrait-associate {
    left: 372px; top: 606px; width: 272px; height: 261px;
    border-radius: 110px 110px 0 0;
    background: linear-gradient(180deg, #7a5238 0%, #3b2a22 45%, #1e2420 100%);
  }
</style>
</head>
<body>
  <main class="flyer">
    <div class="office-photo" role="img" aria-label="Faded photo of hands working with documents and a calculator at an office desk"></div>

    <svg class="accent-circle" width="866" height="867" aria-hidden="true">
      <circle cx="788" cy="891" r="355" fill="var(--gold)"/>
    </svg>

    <div class="brand">
      <div class="brand-row">
        <span class="brand-dot"></span>
        <span class="brand-name">Brightwater Ledger<br>Services, Inc.</span>
      </div>
      <span class="brand-est">EST. 1997</span>
    </div>

    <h1 class="headline">TAX, ACCOUNTING<br><span class="accent">AND BOOKKEEPING</span><br>SERVICES</h1>

    <p class="tagline">We Provide Our Services,<br>With You Next Mortgage In Mind</p>

    <p class="offer">Special Pricing Available for<br>All Mortgage Loan Customers!</p>

    <div class="leader">
      <p class="leader-role">President / CEO</p>
      <p class="leader-name">Marcus Delaney</p>
      <p class="leader-bio">Primary Service Provider with<br>Over 27 Years Of Experience</p>
    </div>

    <div class="portrait portrait-ceo" role="img" aria-label="Photo of a smiling bearded man in glasses and a grey suit holding out a blue calculator"></div>
    <div class="portrait portrait-associate" role="img" aria-label="Portrait photo of a man in a dark suit and silver tie"></div>

    <div class="contact">
      <div class="contact-line">
        <svg class="contact-icon" viewBox="0 0 24 24" aria-hidden="true">
          <circle cx="12" cy="12" r="12" fill="var(--gold)"/>
          <rect x="8" y="5.5" width="8" height="13" rx="1.5" fill="none" stroke="var(--ink)" stroke-width="1.6"/>
          <circle cx="12" cy="15.6" r="0.9" fill="var(--ink)"/>
        </svg>
        <span class="contact-phone">(240) 555-0182</span>
      </div>
      <div class="contact-line">
        <svg class="contact-icon" viewBox="0 0 24 24" aria-hidden="true">
          <circle cx="12" cy="12" r="12" fill="var(--gold)"/>
          <rect x="6" y="7.5" width="12" height="9" rx="1" fill="none" stroke="var(--ink)" stroke-width="1.6"/>
          <path d="M6.5 8.2 L12 12.6 L17.5 8.2" fill="none" stroke="var(--ink)" stroke-width="1.6"/>
        </svg>
        <span class="contact-email">mdelaney@brightwaterledger-example.com</span>
      </div>
    </div>
  </main>
</body>
</html>
```